Business Card Design for Animal Clinic

We are seeking a two sided business card design. The primary side should include our logo (provided in AI and EPS files) address, phone, website, and if possible "Follow Us" with icons for Facebook, Google+, and Twitter.

The back of the card needs to included space for appointment reminders.

Company Name:
Calderbrook Animal Clinic

Doctor Name:
To be provided to winner

Adress:
To be provided to winner

Phone:
to be provided to winner

Website:
www.calderbrookanimalclinic.com

```html
<!DOCTYPE html>
<html lang="en">
<head>
<meta charset="utf-8">
<title>Calderbrook Animal Clinic – Business Card</title>
<link rel="stylesheet" href="https://fonts.googleapis.com/css2?family=Lato:wght@400;700&display=swap">
<style>
  :root {
    --rust: #b85e3b;
    --crimson: #a3232f;
    --peach: #e9a58a;
    --paper: #ffffff;
    --backdrop: #ececec;
    --ink-light: #ffffff;
  }
  html, body {
    margin: 0;
    width: 1200px;
    height: 900px;
    overflow: hidden;
    background: var(--backdrop);
    font-family: "Lato", sans-serif;
  }
  .stage {
    position: relative;
    width: 1200px;
    height: 900px;
  }
  .card {
    position: absolute;
    top: 307px;
    width: 500px;
    height: 286px;
    background: var(--paper);
    box-shadow: 0 6px 18px rgba(0,0,0,0.12);
    overflow: hidden;
  }
  .card--front { left: 70px; }
  .card--back { left: 630px; }
  .card__shapes {
    position: absolute;
    inset: 0;
    width: 100%;
    height: 100%;
  }

  /* Front */
  .brand {
    position: absolute;
    top: 26px;
    left: 0;
    width: 100%;
    margin: 0;
    text-align: center;
    color: var(--crimson);
    font-weight: 400;
  }
  .brand__name {
    display: block;
    font-size: 38px;
    letter-spacing: 3px;
    line-height: 1;
  }
  .brand__sub {
    display: block;
    margin-top: 8px;
    font-size: 15px;
    letter-spacing: 6px;
  }
  .contact {
    position: absolute;
    right: 92px;
    top: 198px;
    text-align: right;
    color: var(--ink-light);
  }
  .contact__doctor {
    font-size: 22px;
    margin: 0 0 4px;
    font-weight: 400;
    line-height: 26px;
  }
  .contact__line {
    margin: 0;
    font-size: 11px;
    letter-spacing: 0.5px;
    text-transform: uppercase;
    line-height: 21px;
    white-space: nowrap;
  }
  .social {
    display: inline-flex;
    gap: 5px;
    vertical-align: middle;
    margin-left: 6px;
  }
  .social__dot {
    width: 15px;
    height: 15px;
    border-radius: 50%;
    background: var(--ink-light);
  }
  .hearts-front {
    position: absolute;
    left: 452px;
    top: 118px;
    width: 20px;
    height: 48px;
    background: var(--crimson);
    border-radius: 6px;
    opacity: 0.85;
  }

  /* Back */
  .reminder__title {
    position: absolute;
    top: 12px;
    left: 28px;
    margin: 0;
    color: var(--ink-light);
    font-size: 13px;
    font-weight: 400;
    letter-spacing: 1px;
    text-transform: uppercase;
  }
  .pets {
    position: absolute;
    left: 390px;
    top: 42px;
    width: 72px;
    height: 52px;
    background: #f6e6dc;
    border-radius: 8px;
  }
  .hearts-back {
    position: absolute;
    left: 456px;
    top: 112px;
    width: 30px;
    height: 26px;
    background: var(--crimson);
    border-radius: 6px;
    opacity: 0.85;
  }
  .slots {
    position: absolute;
    top: 122px;
    left: 28px;
    right: 28px;
    margin: 0;
    padding: 0;
    list-style: none;
  }
  .slot {
    display: flex;
    align-items: flex-end;
    height: 30px;
    font-size: 11.5px;
    color: var(--crimson);
  }
  .slot__label { margin-right: 4px; }
  .slot__line {
    border-bottom: 1.5px dashed var(--peach);
    margin-bottom: 3px;
  }
  .slot__line--date { flex: 1; margin-right: 14px; }
  .slot__line--time { width: 110px; }
</style>
</head>
<body>
<main class="stage">

  <section class="card card--front" aria-label="Business card front">
    <svg class="card__shapes" viewBox="0 0 500 286" preserveAspectRatio="none" aria-hidden="true">
      <path fill="var(--rust)" d="M0,150 C110,100 230,125 300,165 C350,195 405,180 428,100 C436,170 432,240 458,286 L0,286 Z"/>
    </svg>
    <h1 class="brand">
      <span class="brand__name">CALDERBROOK</span>
      <span class="brand__sub">ANIMAL CLINIC</span>
    </h1>
    <div class="hearts-front" role="img" aria-label="Two small hearts"></div>
    <div class="contact">
      <p class="contact__doctor">Dr. Marcus Ellery</p>
      <p class="contact__line">418 N. Harlow Road, Fenwick Springs, FL 32790</p>
      <p class="contact__line">(407) 555-0148 • Follow us:
        <span class="social" aria-label="Social links">
          <span class="social__dot"></span><span class="social__dot"></span><span class="social__dot"></span>
        </span>
      </p>
    </div>
  </section>

  <section class="card card--back" aria-label="Business card back">
    <svg class="card__shapes" viewBox="0 0 500 286" preserveAspectRatio="none" aria-hidden="true">
      <path fill="var(--rust)" d="M0,0 H500 V102 C430,104 380,78 280,62 C170,45 80,42 0,44 Z"/>
    </svg>
    <h2 class="reminder__title">Your next appointment is:</h2>
    <div class="pets" role="img" aria-label="Silhouettes of a dog and two cats sitting together"></div>
    <div class="hearts-back" role="img" aria-label="Two small hearts"></div>
    <ul class="slots">
      <li class="slot"><span class="slot__label">Date:</span><span class="slot__line slot__line--date"></span><span class="slot__label">Time:</span><span class="slot__line slot__line--time"></span></li>
      <li class="slot"><span class="slot__label">Date:</span><span class="slot__line slot__line--date"></span><span class="slot__label">Time:</span><span class="slot__line slot__line--time"></span></li>
      <li class="slot"><span class="slot__label">Date:</span><span class="slot__line slot__line--date"></span><span class="slot__label">Time:</span><span class="slot__line slot__line--time"></span></li>
      <li class="slot"><span class="slot__label">Date:</span><span class="slot__line slot__line--date"></span><span class="slot__label">Time:</span><span class="slot__line slot__line--time"></span></li>
      <li class="slot"><span class="slot__label">Date:</span><span class="slot__line slot__line--date"></span><span class="slot__label">Time:</span><span class="slot__line slot__line--time"></span></li>
    </ul>
  </section>

</main>
</body>
</html>
```